Fresh Produce Outlet needs a Poster Design

Hi,
We are Brightleaf Harvest Market, a fruit and veg outlet based in the suburb of Yanchep, Perth, Western Australia.Apart from fresh produce, we also stock nuts and grains, organic products and specialty grocery. We are about to launch a re-branding exercise, projecting ourselves as 'the' shop for fresh produce; quality, taste and freshness being our key differentiators. We are competing against a big supermarket chain who are using marketing muscle power to shut us down and we want to respond with a series of posters which are simple yet bold and sends a clear and positive message to our customers about what we have to offer.
Please feel free to visit our Facebook page www.facebook.com/brightleafharvestmkt to get an idea about our current branding,logo and the shop in general.
Regards
Team - Brightleaf Harvest Market
Target Market(s)
Residents of Yanchep and surrounding suburbs
Industry/Entity Type
Retail
Look and feel

```html
<!DOCTYPE html>
<html lang="en">
<head>
<meta charset="UTF-8">
<title>Brightleaf Harvest Market – Posters</title>
<link href="https://fonts.googleapis.com/css2?family=Oswald:wght@300;500;700&display=swap" rel="stylesheet">
<style>
  :root {
    --ink: #141414;
    --green: #3fb449;
    --green-dark: #1f8f2e;
    --green-light: #8fd66a;
    --coral: #f2604a;
    --white: #ffffff;
    --veg-red: #d8342a;
    --veg-green: #7fb63e;
    --fruit-orange: #f29a2e;
    --fruit-yellow: #f3d34a;
  }
  * { margin: 0; padding: 0; box-sizing: border-box; }
  html, body { width: 898px; height: 1200px; overflow: hidden; background: var(--white); }
  body { font-family: 'Oswald', sans-serif; position: relative; }

  .poster { position: absolute; left: 0; width: 898px; height: 595px; overflow: hidden; background: var(--white); }
  .poster--veg { top: 0; }
  .poster--fruit { top: 605px; }

  .headline {
    position: absolute; left: 30px; top: 50px;
    font-weight: 700; font-size: 44px; line-height: 0.95;
    text-transform: uppercase; color: var(--ink); letter-spacing: 0.5px;
  }
  .poster--fruit .headline { top: 40px; }
  .headline .accent { color: var(--green); }

  .visit {
    position: absolute; left: 30px; top: 355px;
    font-weight: 700; font-size: 56px; color: var(--coral); letter-spacing: 1px;
  }
  .poster--fruit .visit { top: 355px; }

  .produce-photo { position: absolute; border-radius: 45% 50% 40% 45%; }
  .produce-photo--veg {
    left: 360px; top: 25px; width: 510px; height: 320px;
    background: radial-gradient(ellipse at 60% 35%, var(--veg-green) 0%, #a6cf6a 35%, transparent 70%),
                radial-gradient(ellipse at 25% 65%, var(--veg-red) 0%, #e86a3a 30%, transparent 60%),
                radial-gradient(ellipse at 50% 55%, #f1efe6 0%, #ffffff 80%);
  }
  .produce-photo--fruit {
    left: 420px; top: 15px; width: 450px; height: 330px;
    background: radial-gradient(ellipse at 60% 30%, var(--fruit-yellow) 0%, transparent 55%),
                radial-gradient(ellipse at 35% 60%, #c8312e 0%, transparent 45%),
                radial-gradient(ellipse at 75% 65%, var(--fruit-orange) 0%, transparent 50%),
                radial-gradient(ellipse at 50% 80%, #8bc34a 0%, transparent 45%),
                #ffffff;
  }

  .band { position: absolute; left: 0; bottom: 0; width: 898px; height: 200px; }
  .band svg { display: block; width: 100%; height: 100%; }

  .tagline {
    position: absolute; left: 45px; bottom: 40px;
    font-weight: 300; font-size: 19px; line-height: 1.1;
    color: var(--white); text-transform: uppercase; letter-spacing: 1px;
  }

  .brand-name {
    position: absolute; right: 40px; bottom: 20px;
    font-weight: 700; font-size: 40px; line-height: 0.95;
    color: var(--white); text-transform: uppercase; text-align: right;
  }
</style>
</head>
<body>

<section class="poster poster--veg">
  <div class="produce-photo produce-photo--veg" role="img" aria-label="Assorted fresh vegetables: cabbage, cauliflower, red peppers, onions, chilli and garlic"></div>
  <h1 class="headline">Need<br><span class="accent">Fresh<br>Vegetables</span><br>for the<br><span class="accent">Best Price</span><br>Around?</h1>
  <p class="visit">VISIT US!</p>
  <div class="band">
    <svg viewBox="0 0 898 200" preserveAspectRatio="none" aria-hidden="true">
      <defs>
        <linearGradient id="bandGreenVeg" x1="0" y1="0" x2="1" y2="1">
          <stop offset="0" stop-color="#4cc152"/>
          <stop offset="1" stop-color="#1f8f2e"/>
        </linearGradient>
      </defs>
      <path d="M0 40 Q450 95 898 10 L898 200 L0 200 Z" fill="#8fd66a"/>
      <path d="M0 60 Q450 115 898 30 L898 200 L0 200 Z" fill="#ffffff"/>
      <path d="M0 68 Q450 123 898 38 L898 200 L0 200 Z" fill="url(#bandGreenVeg)"/>
    </svg>
  </div>
  <p class="tagline">The quality<br>you deserve.</p>
  <p class="brand-name">Brightleaf<br>Harvest<br>Market</p>
</section>

<section class="poster poster--fruit">
  <div class="produce-photo produce-photo--fruit" role="img" aria-label="Assorted fresh fruits: bananas, oranges, apples, grapefruit, kiwi and persimmon"></div>
  <h1 class="headline">Need<br><span class="accent">Fresh<br>Fruits</span><br>for the<br><span class="accent">Best Price</span><br>Around?</h1>
  <p class="visit">VISIT US!</p>
  <div class="band">
    <svg viewBox="0 0 898 200" preserveAspectRatio="none" aria-hidden="true">
      <defs>
        <linearGradient id="bandGreenFruit" x1="0" y1="0" x2="1" y2="1">
          <stop offset="0" stop-color="#4cc152"/>
          <stop offset="1" stop-color="#1f8f2e"/>
        </linearGradient>
      </defs>
      <path d="M0 40 Q450 95 898 10 L898 200 L0 200 Z" fill="#8fd66a"/>
      <path d="M0 60 Q450 115 898 30 L898 200 L0 200 Z" fill="#ffffff"/>
      <path d="M0 68 Q450 123 898 38 L898 200 L0 200 Z" fill="url(#bandGreenFruit)"/>
    </svg>
  </div>
  <p class="tagline">The quality<br>you deserve.</p>
  <p class="brand-name">Brightleaf<br>Harvest<br>Market</p>
</section>

</body>
</html>
```